New Alcoholic Spiked Seltzer Line

We need a can design for a line of low calorie alcoholic seltzer. This product is a sparkling water and vodka drink with no sugar added in a slim 12 oz can.

This is a lighter, healthier, alternative to the sugary ready-to-drinks on the market. The product contains only 3 ingredients: Vodka, Water and Natural Flavors. It has only 100 calories but still has 5% alcohol, so you don't need to sacrifice alcohol to cut calories.

This product also does not contain any preservatives.

We want this design to communicate the following objectives to the consumer and in this order:

1. Appetizing product
2.Low calorie
3.Communicate the type of beverage (Spiked Seltzer)

The brand name of the product is VELKA.

The flavor of the product needed to be used for the design is Mango-Orange.

Comparable products are:

www.brisavelfizz.example/
https://www.tarnowbubble.example
https://quellrind.example/

The designs should not infringe or copy the creative directions of the products mentionned above. They are only given so that you can better understand the type of product we are developing.

Target Market(s)

Young Professional women between the ages of 25 and 44

Industry/Entity Type

Product

Colors

Designer to choose colors to be used in the design.

Requirements
Must have
• Design extendibility, meaning it can be adapted for other flavors.
• This is a new category in the market we are targeting, so consumers must easily be able to identify what type of product this is.

```html
<!DOCTYPE html>
<html lang="en">
<head>
<meta charset="utf-8">
<title>VELKA Spiked Seltzer – Can Labels</title>
<link rel="stylesheet" href="https://fonts.googleapis.com/css2?family=Jura:wght@400;500;600&display=swap">
<style>
  :root {
    --bg: #9a9a9a;
    --can-white: #f4f4f4;
    --ink: #1c1c1c;
    --logo-disc: #151515;
    --logo-text: #f4f4f4;
    --mango: #e8892a;
    --mango-soft: #f6cf9a;
    --berry: #c8414a;
    --berry-soft: #eeb6b9;
    --aqua-soft: #d6ecef;
  }
  html, body {
    margin: 0;
    padding: 0;
    width: 1200px;
    height: 960px;
    overflow: hidden;
    background: var(--bg);
  }
  .stage {
    position: relative;
    width: 1200px;
    height: 960px;
  }
  .label {
    position: absolute;
    top: 156px;
    width: 252px;
    height: 660px;
    background: var(--can-white);
    border-radius: 6px;
    overflow: hidden;
    font-family: "Jura", sans-serif;
    color: var(--ink);
  }
  .label--mango { left: 230px; --accent: var(--mango); --accent-soft: var(--mango-soft); }
  .label--berry { left: 634px; --accent: var(--berry); --accent-soft: var(--berry-soft); }

  .label__art {
    position: absolute;
    left: 8px;
    top: 70px;
    width: 236px;
    height: 330px;
  }
  .label__flavor {
    position: absolute;
    margin: 0;
    font-family: "Jura", sans-serif;
    font-weight: 500;
    letter-spacing: 1px;
    line-height: 1;
    transform-origin: left center;
  }
  .label--mango .label__flavor {
    left: 78px;
    top: 272px;
    font-size: 28px;
    transform: rotate(-12deg);
  }
  .label__flavor-line { display: block; }
  .label--berry .label__flavor {
    left: 88px;
    top: 298px;
    font-size: 32px;
    transform: rotate(6deg);
  }

  .brand {
    position: absolute;
    left: 82px;
    top: 372px;
    width: 88px;
    height: 88px;
    border-radius: 50%;
    background: var(--logo-disc);
    display: flex;
    flex-direction: column;
    align-items: center;
    justify-content: center;
  }
  .brand__name {
    font-family: "Jura", sans-serif;
    font-weight: 500;
    font-size: 20px;
    color: var(--logo-text);
    letter-spacing: 1px;
    line-height: 1;
  }
  .brand__tag {
    margin-top: 6px;
    font-size: 5.5px;
    color: var(--logo-text);
    letter-spacing: 0.4px;
  }

  .label__type {
    position: absolute;
    left: 0;
    width: 100%;
    top: 466px;
    margin: 0;
    text-align: center;
    font-size: 18px;
    font-weight: 500;
    line-height: 20px;
  }
  .label__facts {
    position: absolute;
    left: 0;
    width: 100%;
    top: 510px;
    margin: 0;
    text-align: center;
    font-size: 10px;
    font-weight: 600;
    line-height: 11px;
    color: var(--accent);
    letter-spacing: 0.3px;
  }
  .label__band {
    position: absolute;
    left: 0;
    bottom: 0;
    width: 100%;
  }
</style>
</head>
<body>
<main class="stage">

  <section class="label label--mango">
    <svg class="label__art" viewBox="0 0 236 330" role="img" aria-label="Illustration of mango and orange slices and a cocktail glass over dotted and wavy patterns">
      <defs>
        <radialGradient id="mango-glow" cx="50%" cy="35%" r="70%">
          <stop offset="0%" stop-color="var(--mango)"/>
          <stop offset="60%" stop-color="var(--mango-soft)"/>
          <stop offset="100%" stop-color="var(--can-white)"/>
        </radialGradient>
      </defs>
      <ellipse cx="118" cy="165" rx="112" ry="160" fill="url(#mango-glow)"/>
    </svg>
    <h2 class="label__flavor"><span class="label__flavor-line">MANGO-</span><span class="label__flavor-line">ORANGE</span></h2>
    <div class="brand">
      <span class="brand__name">VELKA</span>
      <span class="brand__tag">SPIKED SELTZER</span>
    </div>
    <p class="label__type">Alcoholic<br>Spiked Seltzer</p>
    <p class="label__facts">100 CALORIES<br>5% ALCOHOL</p>
    <svg class="label__band" viewBox="0 0 252 122" height="122" role="img" aria-label="Light blue wavy line pattern">
      <polygon points="0,22 205,0 252,16 252,122 0,122" fill="var(--aqua-soft)"/>
    </svg>
  </section>

  <section class="label label--berry">
    <svg class="label__art" viewBox="0 0 236 330" role="img" aria-label="Illustration of strawberries and a cocktail glass over dotted and wavy patterns">
      <defs>
        <radialGradient id="berry-glow" cx="55%" cy="35%" r="70%">
          <stop offset="0%" stop-color="var(--berry)"/>
          <stop offset="60%" stop-color="var(--berry-soft)"/>
          <stop offset="100%" stop-color="var(--can-white)"/>
        </radialGradient>
      </defs>
      <ellipse cx="118" cy="165" rx="112" ry="160" fill="url(#berry-glow)"/>
    </svg>
    <h2 class="label__flavor">BERRY</h2>
    <div class="brand">
      <span class="brand__name">VELKA</span>
      <span class="brand__tag">SPIKED SELTZER</span>
    </div>
    <p class="label__type">Alcoholic<br>Spiked Seltzer</p>
    <p class="label__facts">100 CALORIES<br>5% ALCOHOL</p>
    <svg class="label__band" viewBox="0 0 252 84" height="84" role="img" aria-label="Light blue wavy line pattern">
      <polygon points="0,26 145,0 252,14 252,84 0,84" fill="var(--aqua-soft)"/>
    </svg>
  </section>

</main>
</body>
</html>
```